Olive Oil label for bottle

BRIEF MODIFICATIONS Two labels: one on the front and the other on the back of the bottle Do not put the DOGS on the front label or on the back label sober design that evokes luxury, freshness, bio, good for health. Favor the black or / and gold colors on a white background or on a black background. make a version on white background typo gold and tree gold make a version on white background typo black and tree black make a version on white background typo black, tree gold, make a version on black background, white typo and white tree make a version on black background, white tpo and gold tree Dimensions of the labels: A - SQUARE / SQUARE FORM SQUARE LABEL Size: 6 cm x 6 cm TEXT OF the label front - front: COLLE DI MURA (CHARACTERS EVEN POLICE, ALL IN CAPS) (PUT THE DRAWING OF THE OLIVE TREE BETWEEN COLLE DI MURA AND OLIO EXTRA VERGINE) OLIO EXTRA VERGINE DI OLIVA CHARACTERS EVEN POLICE, ALL IN CAPITALS) 2019 NOTO - SICILIA B - REAR / BACK LABEL information on the label of the back - back rectangular shape dimensions: height 10 cm, width 6 cm TEXT of the label verso Extra Virgin Olive Oil, first cold pressed, produced from a single terroir in Noto (Sicily). 800 olive trees, untreated, offer this fiery oil, mixture of bitterness and spiciness, without aggressiveness. The harvest made very early in September guarantees fruity aroma and a taste of freshly cut grass. Keep away from light and heat. Owners: Lombrano - Morel 33 6 48 19 53 27 contact@borgalena-estate.example www.borgalena-estate.example put the pictogram of instagram: borgalenaestate Best before 20 May 2022 50 cl - Colle di Mura ©

Target Market(s)

luxury customers Label front - front, type "N ° 8 Valdris

Font styles to use
Sans Serif

Requirements
Should not have
• DOGS DO NOT APPEAR MORE ON LABELS

```html
<!DOCTYPE html>
<html lang="fr">
<head>
<meta charset="utf-8">
<title>Colle di Mura – étiquette arrière</title>
<link rel="stylesheet" href="https://fonts.googleapis.com/css2?family=Libre+Caslon+Text:wght@400;700&family=Noto+Serif:wght@400&display=swap">
<style>
  :root {
    --ink: #111;
    --gold-light: #f6dc7a;
    --gold-mid: #d9b441;
    --gold-deep: #a8801c;
    --band: #050505;
    --paper: #ffffff;
  }
  * { margin: 0; padding: 0; box-sizing: border-box; }
  html, body { width: 1200px; height: 1200px; overflow: hidden; background: var(--paper); }
  .canvas { position: relative; width: 1200px; height: 1200px; }
  .label-shape { position: absolute; left: 0; top: 0; }
  .text { position: absolute; color: var(--ink); font-family: "Libre Caslon Text", Georgia, serif; }
  .storage {
    left: 470px; width: 300px; top: 178px;
    text-align: center; font-weight: 700; font-size: 33px; line-height: 43.5px;
  }
  .description, .harvest {
    left: 405px; width: 425px;
    font-size: 26px; line-height: 36.6px; text-align: justify;
  }
  .description { top: 380px; }
  .description .initial { font-weight: 700; font-size: 36px; }
  .harvest { top: 622px; }
  .best-before {
    left: 380px; width: 480px; top: 806px;
    text-align: center; font-weight: 700; font-size: 30px; line-height: 39px;
  }
  .owners-title {
    left: 500px; width: 240px; top: 930px;
    text-align: center; font-size: 30px; line-height: 36px;
  }
  .contact {
    position: absolute; left: 487px; top: 988px;
    color: #fff; font-family: "Noto Serif", Georgia, serif;
    font-size: 21.5px; line-height: 27.8px; list-style: none;
  }
</style>
</head>
<body>
<main class="canvas">
  <svg class="label-shape" width="1200" height="1200" viewBox="0 0 1200 1200">
    <defs>
      <linearGradient id="gold" x1="0" y1="0" x2="1" y2="1">
        <stop offset="0" stop-color="var(--gold-deep)"/>
        <stop offset="0.3" stop-color="var(--gold-light)"/>
        <stop offset="0.55" stop-color="var(--gold-mid)"/>
        <stop offset="0.8" stop-color="var(--gold-light)"/>
        <stop offset="1" stop-color="var(--gold-deep)"/>
      </linearGradient>
    </defs>
    <!-- label body -->
    <path class="label-outline" d="M358,47 L875,47 C763,110 763,280 875,340 L875,1166 L358,1166 L358,340 C470,280 470,110 358,47 Z"
          fill="url(#gold)" stroke="var(--ink)" stroke-width="4"/>
    <!-- inner frame -->
    <path d="M430,70 L806,70 C720,120 730,300 850,352 L850,955" fill="none" stroke="var(--ink)" stroke-width="3"/>
    <path d="M430,70 C510,120 500,300 384,352 L384,955" fill="none" stroke="var(--ink)" stroke-width="3"/>
    <path d="M371,340 L371,978 M862,340 L862,978" stroke="var(--ink)" stroke-width="3"/>
    <path d="M371,340 C478,290 478,120 403,60 M862,340 C755,290 755,120 830,60" fill="none" stroke="var(--ink)" stroke-width="3"/>
    <!-- crest curve -->
    <path d="M470,124 C540,112 580,134 620,134 C660,134 700,112 770,124" fill="none" stroke="var(--ink)" stroke-width="2.5"/>
    <rect x="578" y="80" width="84" height="62" rx="20" fill="var(--gold-deep)" opacity="0.55" role="img" aria-label="Ornement calligraphique en volutes"/>
    <!-- owners rule -->
    <path d="M362,955 L497,955 M757,955 L872,955" stroke="var(--ink)" stroke-width="3"/>
    <!-- contact band -->
    <rect x="358" y="978" width="517" height="166" fill="var(--band)"/>
    <path d="M358,1144 L875,1144" stroke="var(--ink)" stroke-width="3"/>
    <rect x="394" y="986" width="58" height="140" rx="26" fill="#e8e8e8" role="img" aria-label="Rameau d'olivier blanc"/>
    <!-- icons -->
    <g fill="none" stroke="#fff" stroke-width="2">
      <circle cx="468" cy="1024" r="9"/>
      <path d="M464,1020 l3,3 l-2,3 q2,3 5,5 l3,-2 l3,3" stroke-width="1.8"/>
      <rect x="448" y="1049" width="16" height="11"/>
      <path d="M448,1049 l8,6 l8,-6"/>
      <circle cx="462" cy="1082" r="9"/>
      <path d="M453,1082 h18 M462,1073 v18 M462,1073 q-6,9 0,18 q6,-9 0,-18"/>
    </g>
    <circle cx="467" cy="1112" r="9" fill="#fff"/>
  </svg>

  <h2 class="text storage">À conserver à l’abri de la lumière et de la chaleur.</h2>

  <p class="text description"><span class="initial">H</span>uile d’Olive Extra Vierge produite à partir d’un seul terroir à Noto (Sicile). 800 oliviers, non traités, offrent cette huile ardente, mélange d’amertume et de piquant, sans agressivité.</p>

  <p class="text harvest">La récolte réalisée très tôt en septembre garantit l’arôme fruité et un goût d’herbe fraîchement coupée.</p>

  <p class="text best-before">À consommer de préférence<br>avant le 20 mai 2022</p>

  <h3 class="text owners-title" style="font-weight:400">Propriétaires</h3>

  <ul class="contact">
    <li>Messieurs Lombrano &amp; Morel</li>
    <li>+ 33 6 48 19 53 27</li>
    <li>contact@borgalena-estate.example</li>
    <li>www.borgalena-estate.example</li>
    <li>Instagram: borgalenaestate</li>
  </ul>
</main>
</body>
</html>
```